New Business Card Design Project

Hi! We require a design for business cards for directors and head teachers of an international daycare for children 0 - 9. We are family-owned, -operated and -oriented. We have six locations, looking to franchise. Our USPs are: 1) Flexibility 2) Quality teachers 3) International culture 4) Best nutrition We are quality teachers and professional caretakers, but with creativity and personality! Business cards should be playful (but no Comic Sans or baby hand prints), colorful (but no rainbows), and have some breathing space. It should be obvious from the business card that we're a daycare. In 2020 we'll be launching our new website based on this design: https://plinvo.example/47K2RTWZMPD The font in the new website will be Houschka (medium, demibold, bold). We will keep our current logo, included in the files here. There are also screenshots of some designs we like. Show us your best! :)

Industry/Entity Type

Childcare

Contact Information for Business Card

Femke de Lorre
Communications Wizard
Pluma Tots International Daycare
Voskuilstraat 47 B, 2345 KR Leiden
www.plumatots.example
+31 647153826

Font styles to use
Serif
Sans Serif

Colors

Designer to choose colors to be used in the design.

Requirements
Must have
• Color

```html
<!DOCTYPE html>
<html lang="en">
<head>
<meta charset="utf-8">
<title>Pluma Tots – Business Card</title>
<link rel="stylesheet" href="https://fonts.googleapis.com/css2?family=Fira+Sans:wght@400;500;600&display=swap">
<style>
  :root {
    --bg: #e6e7ea;
    --card: #fbfbfb;
    --pink: #d9427a;
    --blue: #1aa3dc;
    --rule: #a9cde8;
    --sky-top: #dce8f5;
    --sky-bottom: #c0d6ec;
    --tint-pink: rgba(240, 170, 200, 0.45);
    --tint-yellow: rgba(250, 226, 160, 0.45);
    --tint-green: rgba(170, 222, 190, 0.45);
    --tint-lilac: rgba(200, 180, 235, 0.45);
    --shadow: rgba(30, 35, 45, 0.18);
  }
  * { box-sizing: border-box; margin: 0; padding: 0; }
  html, body {
    width: 1200px; height: 1021px; overflow: hidden;
    background: var(--bg);
    font-family: "Fira Sans", sans-serif;
  }
  .stage {
    position: relative; width: 1200px; height: 1021px;
    display: flex; justify-content: center; align-items: center; gap: 60px;
  }
  .card {
    width: 400px; height: 640px;
    box-shadow: 0 12px 30px var(--shadow);
    position: relative; overflow: hidden;
  }
  /* front side */
  .card-front {
    background: var(--card);
    display: flex; flex-direction: column; align-items: center;
    padding-top: 110px; text-align: center;
  }
  .brand-name {
    display: flex; align-items: center; gap: 12px;
    font-size: 46px; font-weight: 600; color: var(--pink);
    line-height: 1; white-space: nowrap;
  }
  .brand-dot {
    width: 22px; height: 22px; border-radius: 50%; background: var(--blue);
  }
  .contact { margin-top: 120px; }
  .person-name { font-size: 24px; font-weight: 500; color: var(--blue); }
  .person-role { font-size: 19px; font-weight: 400; color: var(--pink); margin-top: 2px; }
  .divider { width: 40px; height: 2px; background: var(--rule); margin: 34px auto; }
  .company { font-size: 17px; font-weight: 500; color: var(--blue); }
  .address { font-size: 17px; font-weight: 400; color: var(--pink); margin-top: 2px; }
  .icons { display: flex; justify-content: center; gap: 6px; margin: 16px 0 10px; }
  .icons svg { width: 22px; height: 22px; }
  .phone, .web { font-size: 17px; color: var(--pink); line-height: 1.35; }
  /* back side */
  .card-back { background: var(--sky-bottom); }
  .back-pattern {
    position: absolute; inset: 0;
    background:
      radial-gradient(circle at 18% 14%, var(--tint-yellow), transparent 38%),
      radial-gradient(circle at 85% 26%, var(--tint-pink), transparent 40%),
      radial-gradient(circle at 14% 70%, var(--tint-green), transparent 40%),
      radial-gradient(circle at 82% 84%, var(--tint-lilac), transparent 42%),
      linear-gradient(180deg, var(--sky-top), var(--sky-bottom));
  }
  .back-brand {
    position: absolute; inset: 0;
    display: flex; justify-content: center; align-items: center;
  }
  .back-brand .brand-name { font-size: 52px; }
</style>
</head>
<body>
<main class="stage">
  <section class="card card-front" aria-label="Business card, front">
    <div class="brand-name"><span class="brand-dot"></span>Pluma Tots</div>
    <div class="contact">
      <p class="person-name">Femke de Lorre</p>
      <p class="person-role">Communications Wizard</p>
      <div class="divider"></div>
      <p class="company">Pluma Tots International Daycare</p>
      <p class="address">Voskuilstraat 47 B, 2345 KR Leiden</p>
      <div class="icons">
        <svg viewBox="0 0 24 24" aria-hidden="true">
          <circle cx="12" cy="12" r="11" fill="var(--blue)"/>
          <path d="M8.2 6.5l2 2.3-1.1 1.5c.8 1.7 2 2.9 3.6 3.7l1.5-1.1 2.3 2-1.2 2c-4.2-.4-7.9-4.1-8.3-8.3z" fill="#fff"/>
        </svg>
        <svg viewBox="0 0 24 24" aria-hidden="true">
          <circle cx="12" cy="12" r="11" fill="var(--blue)"/>
          <g fill="none" stroke="#fff" stroke-width="1.3">
            <circle cx="12" cy="12" r="6.5"/>
            <ellipse cx="12" cy="12" rx="3" ry="6.5"/>
            <path d="M5.5 12h13M6.5 8.8h11M6.5 15.2h11"/>
          </g>
        </svg>
      </div>
      <p class="phone">+31 647153826</p>
      <p class="web">www.plumatots.example</p>
    </div>
  </section>

  <section class="card card-back" aria-label="Business card, back">
    <div class="back-pattern" role="img" aria-label="Playful pastel line-drawn pattern of children's doodles in pink, yellow, green and lilac on light blue: clouds, flowers, trees, animals, toys and treats"></div>
    <div class="back-brand">
      <div class="brand-name"><span class="brand-dot"></span>Pluma Tots</div>
    </div>
  </section>
</main>
</body>
</html>
```